Motor Mate 4x6 Flyer

Need 4 x 6 Flyer with following language:

Willow Crest Motor Mate
Our Motor Mate Will Come to Your Home
Our Motor Mate will Drive Your Car to Nearest Gas Station
Our Motor Mate will Fill-up Your Car with Gas
Our Motor Mate will Immediately Return Your Car
Your Car Covered with $100k of Commercial Insurance
Member Dunmore Chamber of Commerce / Honest Merchant League
www.willowcrestmotormate.example

Place logos of Vortan, Brenn & Dorvane on Left Side of Flyer starting at top left corner, mid left side, left bottom corner.
Place logos of BoltNest, 12-Forty, Tesmira on opposite side right.....
Place Willow Crest Motor Mate Logo on both sides of very top that says Willow Crest Motor Mate

Target Market(s)

Upscale Home Owners

Font styles to use
Sans Serif

Colors
F0912C
F2A743
F7CA91
FBE8D2
FDF5EE

Requirements
Must have
• Flyer Must be Bright Orange

```html
<!DOCTYPE html>
<html lang="en">
<head>
<meta charset="utf-8">
<title>Willow Crest Motor Mate Flyer</title>
<link rel="stylesheet" href="https://fonts.googleapis.com/css2?family=Open+Sans:wght@600;700;800&display=swap">
<style>
  :root {
    --orange-top: #f7961b;
    --orange-mid: #e9861a;
    --orange-low: #f9a63b;
    --ink-light: #fdf5ee;
    --badge-bg: #ffffff;
    --badge-ink: #e9861a;
    --title-ink: #f0912c;
  }
  * { margin: 0; padding: 0; box-sizing: border-box; }
  html, body { width: 889px; height: 1200px; overflow: hidden; background: var(--orange-top); }
  .flyer {
    position: relative; width: 889px; height: 1200px; overflow: hidden;
    font-family: "Open Sans", Arial, sans-serif; background: var(--orange-mid);
  }
  .flyer__backdrop { position: absolute; inset: 0; }
  .brand-badge {
    position: absolute; background: var(--badge-bg);
    display: flex; align-items: center; justify-content: center; text-align: center;
    color: var(--badge-ink); font-weight: 700; line-height: 1.1;
  }
  .brand-badge--client { top: 51px; width: 137px; height: 86px; font-size: 19px; }
  .brand-badge--client-left { left: 9px; }
  .brand-badge--client-right { left: 744px; }
  .brand-badge--partner { font-size: 14px; }
  .partner--vortan { left: 40px; top: 218px; width: 95px; height: 38px; font-size: 17px; }
  .partner--boltnest { left: 784px; top: 212px; width: 68px; height: 38px; font-size: 13px; }
  .partner--brenn { left: 42px; top: 560px; width: 86px; height: 79px; font-size: 18px; }
  .partner--twelveforty { left: 786px; top: 576px; width: 60px; height: 54px; font-size: 13px; }
  .partner--dorvane { left: 36px; top: 1095px; width: 72px; height: 60px; font-size: 13px; }
  .partner--tesmira { left: 766px; top: 1105px; width: 82px; height: 50px; font-size: 15px; }
  .title-pill {
    position: absolute; left: 158px; top: 107px; width: 572px; height: 64px;
    background: var(--badge-bg); border-radius: 14px;
    display: flex; align-items: center; justify-content: center;
    color: var(--title-ink); font-size: 38px; font-weight: 800; letter-spacing: 0.2px;
  }
  .service-line {
    position: absolute; left: 0; width: 889px; text-align: center;
    color: var(--ink-light); font-size: 31px; font-weight: 700; line-height: 41px;
  }
  .line--home { top: 205px; }
  .line--drive { top: 347px; }
  .line--fill { top: 542px; }
  .line--return { top: 700px; }
  .line--insurance { top: 859px; }
  .line--member { top: 1012px; }
</style>
</head>
<body>
  <main class="flyer">
    <svg class="flyer__backdrop" width="889" height="1200" viewBox="0 0 889 1200" aria-hidden="true">
      <rect width="889" height="1200" fill="var(--orange-mid)"/>
      <path d="M0 0 H889 V270 C800 500 330 590 0 488 Z" fill="var(--orange-top)"/>
      <path d="M0 925 C320 1010 700 900 889 640 V1200 H0 Z" fill="var(--orange-low)"/>
    </svg>

    <div class="brand-badge brand-badge--client brand-badge--client-left">Motor<br>Mate</div>
    <div class="brand-badge brand-badge--client brand-badge--client-right">Motor<br>Mate</div>
    <h1 class="title-pill">Willow Crest Motor Mate</h1>

    <div class="brand-badge brand-badge--partner partner--vortan">Vortan</div>
    <div class="brand-badge brand-badge--partner partner--boltnest">BoltNest</div>
    <div class="brand-badge brand-badge--partner partner--brenn">Brenn</div>
    <div class="brand-badge brand-badge--partner partner--twelveforty">12-Forty</div>
    <div class="brand-badge brand-badge--partner partner--dorvane">Dorvane</div>
    <div class="brand-badge brand-badge--partner partner--tesmira">Tesmira</div>

    <p class="service-line line--home">Our Motor Mate Will<br>Come to Your Home</p>
    <p class="service-line line--drive">Our Motor Mate will Drive<br>Your Car to Nearest<br>Gas Station</p>
    <p class="service-line line--fill">Our Motor Mate will Fill-up<br>Your Car with Gas</p>
    <p class="service-line line--return">Our Motor Mate will Immediately<br>Return Your Car</p>
    <p class="service-line line--insurance">Your Car Covered with<br>$100k of Commercial Insurance</p>
    <p class="service-line line--member">Member Dunmore Chamber of<br>Commerce / Honest Merchant League</p>
  </main>
</body>
</html>
```